Cover Page for Financial Statements

We need a cover page designed for our Financial Statements. It will need to include our business logo and the Chartered accountant logo.
We have included our current title page ( image titled full.png ) to show all the information that is needed to be included such as the title 'Financial Statements' and 'The year ended March 2023'. We would like to see designs that reflect our logo but also adds some interest with objects / deisngs that fill up more of the page.

Industry/Entity Type

Accounting

Font styles to use
Serif
Sans Serif

Colors

Designer to choose only greyscale colors for use in the design.

Requirements
Must have
• - A4 document size, our logo, Chartered Accountant Logo
Should not have
• Bright Colors

```html
<!DOCTYPE html>
<html lang="en">
<head>
<meta charset="utf-8">
<title>Ledgerline Accounting &amp; Advisory Limited – Financial Statements 2023</title>
<link href="https://fonts.googleapis.com/css2?family=Arimo:wght@400;700&display=swap" rel="stylesheet">
<style>
  :root {
    --stage: #e3e3e3;
    --paper: #ffffff;
    --ink: #111111;
    --ink-soft: #3a3a3a;
    --band-light: #f2f2f2;
    --band-mid: #cfcfcf;
    --band-dark: #9a9a9a;
    --chart-light: #f7f7f7;
    --chart-mid: #d4d4d4;
    --chart-deep: #8a8a8a;
    --footer-bar: #0a0a0a;
  }
  html, body {
    margin: 0;
    padding: 0;
    width: 1200px;
    height: 1200px;
    overflow: hidden;
    background: var(--stage);
    font-family: "Arimo", Arial, sans-serif;
  }
  .cover-page {
    position: absolute;
    left: 228px;
    top: 74px;
    width: 745px;
    height: 1053px;
    background: var(--paper);
    overflow: hidden;
  }
  .cover-art {
    position: absolute;
    inset: 0;
    width: 100%;
    height: 100%;
  }
  .cover-heading {
    position: absolute;
    left: 0;
    right: 0;
    top: 48px;
    text-align: center;
    color: var(--ink);
  }
  .company-name {
    margin: 0;
    font-size: 19px;
    font-weight: 400;
    letter-spacing: 0.1px;
  }
  .document-title {
    margin: 19px 0 0;
    font-size: 39px;
    font-weight: 700;
    letter-spacing: 0.5px;
    line-height: 1;
  }
  .period {
    margin: 10px 0 0;
    font-size: 21px;
    font-weight: 400;
    letter-spacing: 0.3px;
  }
  .partner-mark {
    position: absolute;
    left: 52px;
    top: 907px;
    width: 200px;
    text-align: center;
    color: var(--ink-soft);
    font-weight: 700;
    white-space: nowrap;
  }
  .partner-mark .mark-dot {
    display: block;
    width: 62px;
    height: 62px;
    margin: 0 auto 14px;
    border-radius: 50%;
    background: var(--ink-soft);
  }
  .partner-mark .mark-name {
    display: block;
    font-size: 10px;
    letter-spacing: 1.2px;
  }
  .partner-mark .mark-region {
    display: block;
    margin-top: 4px;
    font-size: 7px;
    letter-spacing: 1px;
  }
  .firm-mark {
    position: absolute;
    right: 62px;
    top: 966px;
    width: 180px;
    text-align: right;
    color: var(--ink);
    font-weight: 400;
    white-space: nowrap;
  }
  .firm-mark .firm-name {
    display: block;
    font-size: 23px;
    letter-spacing: 2.5px;
    line-height: 1;
  }
  .firm-mark .firm-tagline {
    display: block;
    margin-top: 5px;
    font-size: 6.5px;
    letter-spacing: 1.6px;
  }
  .footer-bar {
    position: absolute;
    left: 0;
    right: 0;
    bottom: 0;
    height: 14px;
    background: var(--footer-bar);
  }
</style>
</head>
<body>
  <main class="cover-page">
    <svg class="cover-art" viewBox="0 0 1198 1694" preserveAspectRatio="none">
      <defs>
        <linearGradient id="bandShade" x1="0" y1="0" x2="1" y2="0">
          <stop offset="0" stop-color="var(--band-dark)"/>
          <stop offset="0.35" stop-color="var(--band-light)"/>
          <stop offset="0.75" stop-color="var(--band-mid)"/>
          <stop offset="1" stop-color="var(--band-dark)"/>
        </linearGradient>
        <linearGradient id="chartShade" x1="0" y1="0" x2="1" y2="1">
          <stop offset="0" stop-color="var(--chart-mid)"/>
          <stop offset="0.55" stop-color="var(--chart-light)"/>
          <stop offset="1" stop-color="var(--chart-deep)"/>
        </linearGradient>
      </defs>
      <rect class="photo-band" x="0" y="329" width="1198" height="941" fill="url(#bandShade)"
            role="img" aria-label="Blurred office background behind the financial graphics"/>
      <polygon class="glass-panel" points="319,537 921,420 921,1320 319,1433" fill="#f4f4f4" opacity="0.55"/>
      <polygon class="chart-illustration" points="86,529 713,414 713,1272 86,1382" fill="url(#chartShade)" opacity="0.92"
               role="img" aria-label="Hand holding a tablet with floating pie chart, bar chart and line graph"/>
      <polyline class="frame-line" points="392,329 1016,397 1016,1270" fill="none" stroke="#ffffff" stroke-width="3"/>
      <polyline class="frame-line" points="392,1270 392,1227 720,1280" fill="none" stroke="#ffffff" stroke-width="3"/>
      <polygon class="frame-line" points="469,429 1099,542 1099,1492 469,1382" fill="none" stroke="#ffffff" stroke-width="3" opacity="0.9"/>
    </svg>

    <header class="cover-heading">
      <p class="company-name">Ledgerline Accounting &amp; Advisory Limited</p>
      <h1 class="document-title">FINANCIAL STATEMENTS</h1>
      <p class="period">FOR THE YEAR ENDED 31 MARCH 2023</p>
    </header>

    <div class="partner-mark">
      <span class="mark-dot"></span>
      <span class="mark-name">CERTIFIED ACCOUNTANTS</span>
      <span class="mark-region">GUILD · OCEANIA</span>
    </div>

    <div class="firm-mark">
      <span class="firm-name">LEDGERLINE</span>
      <span class="firm-tagline">ACCOUNTING &amp; ADVISORY</span>
    </div>

    <div class="footer-bar"></div>
  </main>
</body>
</html>
```